" A Lunar Petal Studio é uma pequena empresa, localizada nos Estados Unidos, especializada em criar produtos personalizados para celebrações, como cake toppers, papelaria para festas e peças em papel, acrílico e madeira cortadas a laser. Cada produto é desenvolvido sob encomenda, com foco em qualidade, delicadeza e atenção aos detalhes, proporcionando uma experiência única e memorável para cada cliente. "

```html
<!DOCTYPE html>
<html lang="pt">
<head>
<meta charset="utf-8">
<title>Lunar Petal Studio – Assinatura</title>
<link href="https://fonts.googleapis.com/css2?family=Arimo:wght@400;600&display=swap" rel="stylesheet">
<style>
  :root {
    --page-bg: #f4f1ec;
    --card-bg: #e4edf8;
    --brand-brown: #6b4a3c;
    --contact-text: #3d3d3d;
    --stripe-pink: #f0b3a8;
    --mark-pink: #f7d9d3;
    --mark-ring: #fbeeea;
    --checker-tone: #eef1f5;
  }
  * { margin: 0; padding: 0; box-sizing: border-box; }
  html, body {
    width: 1200px;
    height: 1200px;
    overflow: hidden;
    background: var(--page-bg);
    font-family: "Arimo", Arial, sans-serif;
  }
  .signature {
    position: absolute;
    left: 60px;
    top: 485px;
    width: 1080px;
    height: 230px;
    background: var(--card-bg);
    overflow: hidden;
  }
  .brand-mark {
    position: absolute;
    left: 22px;
    top: 20px;
    width: 150px;
    height: 150px;
    border-radius: 50%;
    background: var(--mark-pink);
    border: 10px solid var(--mark-ring);
  }
  .brand-name {
    position: absolute;
    left: 190px;
    top: 58px;
    width: 290px;
    color: var(--brand-brown);
    font-weight: 600;
    font-size: 38px;
    line-height: 44px;
  }
  .brand-tagline {
    position: absolute;
    left: 190px;
    top: 152px;
    color: var(--brand-brown);
    font-size: 13px;
    letter-spacing: 0.5px;
  }
  .contact-list {
    position: absolute;
    left: 605px;
    top: 18px;
    list-style: none;
  }
  .contact-item {
    display: flex;
    align-items: center;
    gap: 14px;
    height: 34px;
    margin-bottom: 46px;
    color: var(--contact-text);
    font-size: 25px;
  }
  .contact-dot {
    width: 24px;
    height: 24px;
    border-radius: 50%;
    border: 2.5px solid var(--contact-text);
  }
  .contact-square {
    width: 24px;
    height: 24px;
    border-radius: 5px;
    border: 2.5px solid var(--contact-text);
  }
  .stripe-thick {
    position: absolute;
    left: 0;
    top: 188px;
    width: 972px;
    height: 10px;
    background: var(--stripe-pink);
  }
  .stripe-thin {
    position: absolute;
    left: 0;
    top: 204px;
    width: 972px;
    height: 4px;
    background: var(--stripe-pink);
  }
  .transparency-area {
    position: absolute;
    right: 0;
    top: 0;
    width: 108px;
    height: 230px;
    background: var(--checker-tone);
  }
</style>
</head>
<body>
  <section class="signature">
    <div class="brand-mark"></div>
    <div class="brand-name">Lunar Petal Studio</div>
    <div class="brand-tagline">Custom Toppers &amp; Laser Crafts</div>

    <ul class="contact-list">
      <li class="contact-item"><span class="contact-dot"></span>(555)014-2290</li>
      <li class="contact-item"><span class="contact-square"></span>@lunarpetal.studio</li>
    </ul>

    <div class="stripe-thick"></div>
    <div class="stripe-thin"></div>
    <div class="transparency-area" role="img" aria-label="Transparent background area shown as a light checker pattern"></div>
  </section>
</body>
</html>
```